" Serviços oferecidos 1. Palestras motivacionais para empresas ou instituições; 2. Atividade física e fisioterapia para populações especiais; a. Por necessidades especiais entende-se pessoas com doenças neurológicas (alzheimer, parkinson, etc), diabéticos, obesos, depressão, ansiedade, idosos). Além disso, se enquadram crianças e atletas da categoria master, que desejam participar de competições. 3. Massagem relaxante (quick massage, shiatsu), terapia manual, isostretching. "

```html
<!DOCTYPE html>
<html lang="pt-BR">
<head>
<meta charset="UTF-8">
<title>Vértice – Cartão de Visita</title>
<link href="https://fonts.googleapis.com/css2?family=Montserrat:wght@400;500;600;700&display=swap" rel="stylesheet">
<style>
  :root {
    --teal: #1e4948;
    --teal-dark: #173a39;
    --orange: #d9802c;
    --white: #ffffff;
    --paper: #f4f4f2;
    --ink: #1b1b1b;
    --grey: #6f7474;
    --backdrop: #e6e7e5;
  }
  * { box-sizing: border-box; margin: 0; padding: 0; }
  html, body { width: 1200px; height: 1200px; overflow: hidden; }
  body {
    background: var(--backdrop);
    font-family: "Montserrat", Arial, sans-serif;
    display: flex;
    flex-direction: column;
    align-items: center;
    justify-content: center;
    gap: 48px;
  }
  .card {
    width: 740px;
    height: 420px;
    position: relative;
    overflow: hidden;
    border-radius: 6px;
    box-shadow: 0 6px 18px rgba(0,0,0,.12);
  }

  /* Front */
  .card--front { background: var(--teal); }
  .front-brand {
    position: absolute; left: 0; right: 0; top: 120px;
    display: flex; flex-direction: column; align-items: center;
  }
  .brand { display: flex; align-items: center; gap: 16px; color: var(--white); }
  .brand__dot { width: 58px; height: 58px; border-radius: 50%; background: var(--orange); }
  .brand__name { font-weight: 600; font-size: 78px; letter-spacing: 1px; line-height: 1; }
  .brand__tagline {
    margin-top: 8px; margin-left: 74px;
    font-size: 11px; letter-spacing: 1.5px; text-transform: uppercase; color: var(--orange);
  }
  .front-tabs {
    position: absolute; left: 70px; right: 70px; bottom: 0; height: 22px; display: flex;
  }
  .front-tabs__orange { flex: 0 0 54%; background: var(--orange); border-radius: 22px 0 0 0; }
  .front-tabs__white { flex: 1; background: var(--white); border-radius: 0 22px 0 0; }

  /* Back */
  .card--back { background: var(--paper); display: flex; flex-direction: column; }
  .back-top {
    flex: 0 0 205px; display: flex; align-items: center; padding: 0 60px;
  }
  .back-top .brand { color: var(--teal); gap: 12px; }
  .back-top .brand__dot { width: 40px; height: 40px; }
  .back-top .brand__name { font-size: 52px; }
  .person { margin-left: auto; margin-right: 40px; text-align: center; }
  .person__name { font-weight: 700; font-size: 22px; color: var(--ink); letter-spacing: .5px; }
  .person__role { margin-top: 18px; font-size: 12px; color: var(--grey); text-transform: uppercase; }
  .back-rule { height: 8px; display: flex; }
  .back-rule__grey { flex: 0 0 62%; background: #d4d6d5; }
  .back-rule__orange { flex: 1; background: var(--orange); }
  .back-bottom {
    flex: 1; background: var(--teal); color: var(--white);
    display: grid; grid-template-columns: 1fr 1fr; column-gap: 30px;
    padding: 36px 56px 0 56px; align-content: start; row-gap: 30px;
  }
  .contact { display: flex; align-items: flex-start; gap: 16px; font-size: 17px; font-weight: 600; }
  .contact svg { flex: 0 0 20px; width: 20px; height: 20px; margin-top: 1px; }
  .contact__lines { display: flex; flex-direction: column; gap: 4px; }
  .contact--small { font-size: 14px; line-height: 1.35; }
  .contact__cep { font-size: 10px; font-weight: 500; }
</style>
</head>
<body>

  <section class="card card--front" aria-label="Frente do cartão">
    <div class="front-brand">
      <div class="brand">
        <span class="brand__dot"></span>
        <span class="brand__name">Vértice</span>
      </div>
      <p class="brand__tagline">Movimento, saúde &amp; bem-estar</p>
    </div>
    <div class="front-tabs">
      <span class="front-tabs__orange"></span>
      <span class="front-tabs__white"></span>
    </div>
  </section>

  <section class="card card--back" aria-label="Verso do cartão">
    <div class="back-top">
      <div class="brand">
        <span class="brand__dot"></span>
        <span class="brand__name">Vértice</span>
      </div>
      <div class="person">
        <p class="person__name">NOME SOBRENOME</p>
        <p class="person__role">Função</p>
      </div>
    </div>
    <div class="back-rule"><span class="back-rule__grey"></span><span class="back-rule__orange"></span></div>
    <div class="back-bottom">
      <div class="contact">
        <svg viewBox="0 0 20 20" aria-hidden="true"><rect x="2" y="4" width="16" height="12" rx="1.5" fill="none" stroke="#fff" stroke-width="1.8"/><path d="M2.5 5 10 11 17.5 5" fill="none" stroke="#fff" stroke-width="1.8"/></svg>
        <span>empresa@.com.br</span>
      </div>
      <div class="contact">
        <svg viewBox="0 0 20 20" aria-hidden="true"><circle cx="10" cy="10" r="8" fill="none" stroke="#fff" stroke-width="1.6"/><ellipse cx="10" cy="10" rx="3.5" ry="8" fill="none" stroke="#fff" stroke-width="1.4"/><path d="M2 10h16" stroke="#fff" stroke-width="1.4"/></svg>
        <span>www.empresa.com.br</span>
      </div>
      <div class="contact contact--small">
        <svg viewBox="0 0 20 20" aria-hidden="true"><path d="M5 3c1 0 2 2.5 2 3.2S5.6 7.6 5.6 8.2c.6 2 3.2 4.6 5.2 5.2.6 0 1.4-1.4 2-1.4S17 13 17 14s-1.6 3-3 3C9 17 3 11 3 6c0-1.4 1-3 2-3z" fill="#fff"/></svg>
        <span class="contact__lines"><span>(11) 0000-0000</span><span>(11) 00000-0000</span></span>
      </div>
      <div class="contact contact--small">
        <svg viewBox="0 0 20 20" aria-hidden="true"><path d="M10 1.5a6 6 0 0 0-6 6c0 4.5 6 11 6 11s6-6.5 6-11a6 6 0 0 0-6-6z" fill="#fff"/><circle cx="10" cy="7.5" r="2.2" fill="var(--teal)"/></svg>
        <span class="contact__lines"><span>Rua do projeto, 00 Centro -</span><span>Cidade - Estado - <span class="contact__cep">Cep. 00.000.000</span></span></span>
      </div>
    </div>
  </section>

</body>
</html>
```